Services Brochure

We need an revised brochure for our 3 main services. I have uploaded our old Brochure for reference. We have 3 main services (Managed IT Services, Business VoIP, Business Internet). Below is some text we would like included in the brochure for each service section. In addition I have attached a "mock up" showing that we want IT Services on top, VoIP in the middle and Internet at the bottom. Please use your design experience to select images that would fit well. I also included an image of the phone we would like to use.
Text for Brochure:
Title/Header: Unleash the Power of Local IT Solutions
IT Services That Mean Business
Experience fanatical customer service with our affordable, full-service IT solutions. We’re 100% local, ensuring leading response times and personalized support—so you can focus on what you do best.
Talk More, Worry Less with Our Telephone Services
Say goodbye to overpriced equipment and hello to our free phone plan. Keep your number and enjoy unlimited local and long-distance calling. Tailor your phone system to your business needs and rest assured—our rates are always the lowest in town.
Highspeed Internet That Sets You Apart
Stay connected with blazing-fast speeds—from 1Gbps to 10Gbps, both up and down. Benefit from a static IP address and unbeatable prices, backed by 100% local support. Get the connectivity your business deserves at the best value in town.
Elevate your business with cutting-edge technology.
Sorry everyone the banner size is 81" high and 33" wide.

```html
<!DOCTYPE html>
<html lang="en">
<head>
<meta charset="utf-8">
<title>Norvex Services Brochure</title>
<link rel="stylesheet" href="https://fonts.googleapis.com/css2?family=Outfit:wght@400;500&family=Poppins:ital,wght@0,600;0,700;0,800;1,800;1,900&display=swap">
<style>
  :root {
    --page: #8a8889;
    --paper: #f3f3f5;
    --panel: #e1e1e4;
    --navy: #2b3186;
    --azure: #1581c6;
    --cyan: #35c3d8;
    --ink: #3a3a3f;
    --muted: #8b8b92;
    --footer: #23252d;
    --white: #ffffff;
  }
  * { box-sizing: border-box; margin: 0; padding: 0; }
  html, body { width: 1200px; height: 1200px; overflow: hidden; }
  body { background: var(--page); position: relative; font-family: "Outfit", sans-serif; }

  .brochure {
    position: absolute; left: 160px; top: 31px;
    width: 880px; height: 1138px;
    background: linear-gradient(160deg, #fafafb, var(--paper) 55%, #ececef);
    overflow: hidden;
  }

  .hero { position: absolute; left: 0; top: 0; width: 880px; height: 317px; }
  .hero-photo {
    position: absolute; inset: 0;
    background:
      radial-gradient(ellipse at 30% 20%, rgba(120,160,210,.55), transparent 55%),
      radial-gradient(ellipse at 85% 60%, rgba(200,210,225,.35), transparent 40%),
      linear-gradient(180deg, #2a4266 0%, #0f1c30 60%, #0a1220 100%);
  }
  .brand {
    position: absolute; top: 38px; left: 0; width: 100%;
    text-align: center; color: var(--white);
    font-family: "Poppins", sans-serif; font-weight: 600;
    font-size: 56px; line-height: 64px; letter-spacing: 1px;
  }
  .headline {
    position: absolute; top: 128px; left: 0; width: 100%;
    text-align: center; font-family: "Poppins", sans-serif; font-weight: 800;
    font-size: 51px; line-height: 49px; color: var(--white);
    text-transform: uppercase; letter-spacing: -0.5px;
  }
  .headline .accent { color: var(--cyan); }

  .service {
    position: absolute; left: 51px; width: 779px;
    background: var(--panel); border-radius: 20px;
  }
  .service-title {
    height: 48px; border-radius: 20px 20px 0 0;
    background: linear-gradient(90deg, var(--navy), var(--azure) 55%, var(--navy));
    color: var(--white); font-family: "Poppins", sans-serif;
    font-style: italic; font-weight: 900; font-size: 24px; line-height: 48px;
    letter-spacing: -0.3px; padding-left: 29px;
  }
  .service-title.centered { padding-left: 0; text-align: center; }
  .points { position: absolute; list-style: none; color: var(--ink); font-size: 15.5px; line-height: 19px; }
  .points li { position: relative; padding-left: 16px; margin-bottom: 5.5px; }
  .points li svg { position: absolute; left: 0; top: 5px; }

  .svc-it { top: 356px; height: 199px; }
  .svc-it .points { left: 26px; top: 64px; width: 470px; }
  .svc-it .points li { margin-bottom: 5.5px; }
  .photo-it {
    position: absolute; left: 496px; top: 0; width: 283px; height: 199px;
    border-radius: 0 20px 20px 0;
    background: linear-gradient(90deg, rgba(225,225,228,0), #c9c3c0 25%, #8e8a8c 60%, #4c4d55);
  }

  .svc-phone { top: 571px; height: 200px; }
  .photo-phone {
    position: absolute; left: 0; top: 48px; width: 233px; height: 152px;
    border-radius: 0 0 0 20px;
    background: linear-gradient(90deg, #4d4e52, #8c8d91 50%, rgba(225,225,228,0));
  }
  .svc-phone .points { left: 236px; top: 73px; width: 520px; }

  .svc-net { top: 792px; height: 199px; }
  .svc-net .points { left: 26px; top: 66px; width: 500px; }
  .photo-net {
    position: absolute; left: 541px; top: -51px; width: 224px; height: 250px;
    background: linear-gradient(180deg, rgba(40,30,30,.75) 0%, #e9e9ee 30%, #d8dce4 55%, #6f88ad 85%, #b89a72 100%);
    border-radius: 110px 110px 0 0;
  }

  .tagline {
    position: absolute; top: 1004px; left: 0; width: 100%; text-align: center;
    font-family: "Poppins", sans-serif; font-style: italic; font-weight: 900;
    font-size: 24px; letter-spacing: -0.4px; color: var(--muted);
  }
  .tagline strong { color: var(--navy); font-weight: 900; }

  .footer { position: absolute; left: 0; top: 1074px; width: 880px; height: 64px; background: var(--footer); }
  .footer-shape { position: absolute; left: 0; top: 1064px; }
  .contact {
    position: absolute; display: flex; align-items: center; gap: 6px;
    color: var(--white); font-family: "Poppins", sans-serif; font-weight: 600;
  }
  .contact-email { left: 31px; top: 1091px; font-size: 17px; }
  .contact-phone { left: 305px; top: 1083px; font-size: 30px; font-weight: 700; letter-spacing: 0.5px; }
  .contact-web { left: 659px; top: 1092px; font-size: 17px; }
</style>
</head>
<body>
<main class="brochure">
  <header class="hero">
    <div class="hero-photo" role="img" aria-label="Two technicians working in a server room, one wearing a VR headset"></div>
    <div class="brand">Norvex</div>
    <h1 class="headline">Unleash the<br>Power of Local<br><span class="accent">IT Solutions</span></h1>
  </header>

  <section class="service svc-it">
    <h2 class="service-title">IT Services That Mean Business</h2>
    <div class="photo-it" role="img" aria-label="Smiling man typing at a desktop computer"></div>
    <ul class="points">
      <li><svg width="9" height="11" viewBox="0 0 9 11"><path d="M1.5 1 L7 5.5 L1.5 10" fill="none" stroke="#555" stroke-width="2"/></svg>Experience fanatical customer service</li>
      <li><svg width="9" height="11" viewBox="0 0 9 11"><path d="M1.5 1 L7 5.5 L1.5 10" fill="none" stroke="#555" stroke-width="2"/></svg>with our affordable</li>
      <li><svg width="9" height="11" viewBox="0 0 9 11"><path d="M1.5 1 L7 5.5 L1.5 10" fill="none" stroke="#555" stroke-width="2"/></svg>full-service IT solutions.</li>
      <li><svg width="9" height="11" viewBox="0 0 9 11"><path d="M1.5 1 L7 5.5 L1.5 10" fill="none" stroke="#555" stroke-width="2"/></svg>We’re 100% local ensuring leading response times and personalized support—so you can focus on what you do best.</li>
    </ul>
  </section>

  <section class="service svc-phone">
    <h2 class="service-title centered">Talk More, Worry Less with Our Telephone Services</h2>
    <div class="photo-phone" role="img" aria-label="Hand lifting the receiver of an office desk phone"></div>
    <ul class="points">
      <li><svg width="9" height="11" viewBox="0 0 9 11"><path d="M1.5 1 L7 5.5 L1.5 10" fill="none" stroke="#555" stroke-width="2"/></svg>Say goodbye to overpriced equipment and hello to our free phone plan.</li>
      <li><svg width="9" height="11" viewBox="0 0 9 11"><path d="M1.5 1 L7 5.5 L1.5 10" fill="none" stroke="#555" stroke-width="2"/></svg>Keep your number and enjoy unlimited local and long-distance calling.</li>
      <li><svg width="9" height="11" viewBox="0 0 9 11"><path d="M1.5 1 L7 5.5 L1.5 10" fill="none" stroke="#555" stroke-width="2"/></svg>Tailor your phone system to your business needs and rest assured —our rates are always the lowest in town.</li>
    </ul>
  </section>

  <section class="service svc-net">
    <h2 class="service-title">Highspeed Internet That Sets You Apart</h2>
    <div class="photo-net" role="img" aria-label="Excited woman sitting on a chair with a laptop"></div>
    <ul class="points">
      <li><svg width="9" height="11" viewBox="0 0 9 11"><path d="M1.5 1 L7 5.5 L1.5 10" fill="none" stroke="#555" stroke-width="2"/></svg>Stay connected with blazing-fast speeds—from 1Gbps to 10Gbps, both up and down</li>
      <li><svg width="9" height="11" viewBox="0 0 9 11"><path d="M1.5 1 L7 5.5 L1.5 10" fill="none" stroke="#555" stroke-width="2"/></svg>Benefit from a static IP address and unbeatable prices, backed by 100% local support.</li>
      <li><svg width="9" height="11" viewBox="0 0 9 11"><path d="M1.5 1 L7 5.5 L1.5 10" fill="none" stroke="#555" stroke-width="2"/></svg>Get the connectivity your business deserves at the best value in town.</li>
    </ul>
  </section>

  <p class="tagline">Elevate your business with <strong>cutting-edge technology</strong></p>

  <footer>
    <div class="footer"></div>
    <svg class="footer-shape" width="880" height="74" viewBox="0 0 880 74">
      <polygon points="235,0 651,0 604,74 283,74" fill="#2b3186"/>
    </svg>
    <div class="contact contact-email">
      <svg width="22" height="16" viewBox="0 0 22 16"><rect x="1" y="1" width="20" height="14" fill="none" stroke="#fff" stroke-width="1.5"/><path d="M1 1 L11 9 L21 1 M1 15 L8 7 M21 15 L14 7" fill="none" stroke="#fff" stroke-width="1.3"/></svg>
      sales@norvexit.com
    </div>
    <div class="contact contact-phone">
      <svg width="24" height="30" viewBox="0 0 24 30"><path d="M6 3 L10 3 L11 9 L8 11 Q10 18 15 22 L18 19 L23 21 L22 26 Q18 29 13 26 Q4 19 3 8 Q3 4 6 3 Z" fill="#fff"/></svg>
      555-014-2378
    </div>
    <div class="contact contact-web">
      <svg width="18" height="18" viewBox="0 0 18 18" fill="none" stroke="#fff" stroke-width="1.2"><circle cx="9" cy="9" r="8"/><ellipse cx="9" cy="9" rx="3.5" ry="8"/><path d="M1 9 H17 M2.5 5 H15.5 M2.5 13 H15.5"/></svg>
      www.norvexit.com
    </div>
  </footer>
</main>
</body>
</html>
```